Thrive Hollow Wording For Logo & Business card

I have the logo, I just need the "thrive Hollow" wording to go with it, and a business card design. The only thing on the business card is the website info. We provide nature connection experiences, and bolster these efforts through writing and host a platform for community around it.

I also have an idea of what it could look like (sketch), though I'm really not sure how it would come out. I am open to the best design and happy to consider original artwork. You can see what the site is about at ThriveHollow.com.

Contact Information for Business Card

The only thing on the business card is the website info and the design. I will put other messaging on the back.

Website lettering (ThriveHollow.com) in Montserrat

Logo Text

Thrive Hollow (letters optional)

Font styles to use
Other font styles liked:
• montserrat

```html
<!DOCTYPE html>
<html lang="en">
<head>
<meta charset="utf-8">
<title>Thrive Hollow — Business Card</title>
<link rel="stylesheet" href="https://fonts.googleapis.com/css2?family=Audiowide&family=Montserrat:wght@400;500&display=swap">
<style>
  :root {
    --backdrop: #ef6e4f;
    --card-light: #ffffff;
    --card-dark: #0b0324;
    --ink: #1a0f2e;
    --ember: #c8402a;
    --glow: #fbf5a8;
    --flame: #f6a623;
  }
  * { margin: 0; padding: 0; box-sizing: border-box; }
  html, body {
    width: 1122px;
    height: 1200px;
    overflow: hidden;
    background: var(--backdrop);
  }
  .canvas {
    position: relative;
    width: 1122px;
    height: 1200px;
  }
  .card {
    position: absolute;
    left: 133px;
    width: 861px;
    height: 491px;
    overflow: hidden;
  }
  .card--front { top: 71px; background: var(--card-light); }
  .card--back  { top: 607px; background: var(--card-dark); }

  .brand-disc {
    position: absolute;
    left: 336px;
    top: 60px;
    width: 188px;
    height: 188px;
    border-radius: 50%;
    background: var(--card-dark);
  }
  .wordmark {
    position: absolute;
    left: 0;
    right: 0;
    top: 278px;
    text-align: center;
    font-family: "Audiowide", sans-serif;
    font-size: 40px;
    line-height: 52px;
    color: var(--ink);
  }
  .web-band {
    position: absolute;
    top: 394px;
    height: 15px;
  }
  .web-band--left {
    left: 0;
    width: 292px;
    background: linear-gradient(to right, var(--ember), var(--glow));
  }
  .web-band--right {
    left: 569px;
    right: 0;
    background: linear-gradient(to left, var(--ember), var(--glow));
  }
  .website {
    position: absolute;
    left: 292px;
    width: 277px;
    top: 387px;
    text-align: center;
    font-family: "Montserrat", sans-serif;
    font-weight: 400;
    font-size: 21px;
    line-height: 28px;
    color: var(--ink);
    letter-spacing: 0.2px;
  }
  .back-name {
    position: absolute;
    left: 0;
    right: 0;
    top: 220px;
    text-align: center;
    font-family: "Audiowide", sans-serif;
    font-size: 44px;
    line-height: 54px;
    color: var(--flame);
  }
</style>
</head>
<body>
  <main class="canvas">
    <section class="card card--front">
      <div class="brand-disc"></div>
      <h1 class="wordmark">Thrive Hollow</h1>
      <div class="web-band web-band--left"></div>
      <p class="website">www.thrivehollow.com</p>
      <div class="web-band web-band--right"></div>
    </section>
    <section class="card card--back">
      <p class="back-name">Thrive Hollow</p>
    </section>
  </main>
</body>
</html>
```